Human Resources Flyer design

Create a 1 page flyer design for a staffing company that is looking to provide its services to clients. Images centered around people and businesses.
Target Market(s)
Large businesses
Industry/Entity Type
Staffing
Requirements
Must have
- Use color scheme that matches norvelhire.example.
Nice to have
- Flow chart like image for 3 areas mentioned.
- Images that convey professionalism and people connections

```html
<!DOCTYPE html>
<html lang="en">
<head>
<meta charset="utf-8">
<title>Norvel Hire – Staffing Flyer</title>
<link href="https://fonts.googleapis.com/css2?family=Lato:wght@400;700&display=swap" rel="stylesheet">
<style>
:root{
  --stage:#8a8a8a;
  --paper:#ffffff;
  --red:#d42a2f;
  --red-deep:#a8141c;
  --slate:#5f6b7c;
  --slate-dark:#2e3744;
  --ink:#2b2b2b;
  --heading-red:#b5121b;
}
*{margin:0;padding:0;box-sizing:border-box}
html,body{width:1200px;height:840px;overflow:hidden;background:var(--stage);font-family:'Lato',sans-serif}
.sheet{position:absolute;top:60px;width:511px;height:704px;background:var(--paper);box-shadow:0 4px 14px rgba(0,0,0,.35)}
.sheet--front{left:62px}
.sheet--back{left:627px}
.art{position:absolute;left:16px;top:16px;width:479px;height:672px;overflow:hidden;background:linear-gradient(135deg,var(--red) 0%,var(--red-deep) 100%)}
.art svg.shapes{position:absolute;inset:0}
.brand{position:absolute;display:flex;align-items:center;gap:8px;color:#fff;font-weight:700;letter-spacing:3px}
.brand__mark{width:14px;height:14px;background:#fff}
.front-title{position:absolute;left:32px;top:158px;color:#fff;font-size:20px;font-weight:400}
.front-sub{position:absolute;left:33px;top:188px;color:#fff;font-size:10.5px}
.front-copy{position:absolute;right:26px;display:flex;flex-direction:column;align-items:flex-end;color:#fff;font-size:13px;line-height:16.8px}
.front-copy--pitch{top:342px;font-weight:700}
.front-copy--quote{top:444px;font-weight:400;letter-spacing:.2px}
.front-copy__line{white-space:nowrap;text-align:justify;text-align-last:justify}
.front-copy__line--end{text-align-last:left}
.front-url{position:absolute;left:0;top:618px;width:250px;height:24px;background:linear-gradient(90deg,rgba(95,107,124,.85),rgba(95,107,124,.6));color:#fff;font-size:12.5px;line-height:24px;padding-left:50px}
.stage-ring{position:absolute;color:#fff;font-size:12.5px;text-align:center;line-height:15px;width:110px}
.expect-band{position:absolute;left:0;top:220px;width:479px;height:22px;background:linear-gradient(90deg,#fff 0%,#f4d3cc 45%,rgba(212,42,47,0) 100%)}
.expect-title{position:absolute;left:34px;top:223px;color:var(--heading-red);font-weight:700;font-size:12px}
.intro{position:absolute;left:34px;top:249px;color:#fff;font-size:10.5px}
.stage{position:absolute;left:26px;width:430px;color:#fff}
.stage__head{display:flex;align-items:center;gap:10px;font-size:11.5px}
.stage__head span{border-bottom:1px solid #fff;padding-bottom:1px}
.stage__icon{width:18px;height:18px;border:1.5px solid #fff;border-radius:2px}
.stage__text{margin:8px 0 6px 8px;font-size:8.6px;line-height:11px}
.stage__list{list-style:none;margin-left:8px;font-size:7.4px;line-height:9.3px}
.stage__list li{padding-left:10px;position:relative}
.stage__list li::before{content:"✓";position:absolute;left:0}
.contact{position:absolute;left:34px;top:632px;font-size:9px;color:var(--ink)}
.contact b{margin-right:4px}
.contact__mail{position:absolute;left:58px;top:13px;white-space:nowrap}
.socials{position:absolute;left:214px;top:630px;display:flex;gap:10px}
.socials i{width:16px;height:16px;border:1.5px solid var(--red);border-radius:50%}
.back-brand{position:absolute;right:36px;top:612px;color:var(--red);font-weight:700;font-size:17px;letter-spacing:2px;display:flex;align-items:center;gap:6px}
.back-brand i{width:12px;height:12px;background:var(--red)}
.back-url{position:absolute;right:40px;top:644px;font-size:8px;color:var(--ink)}
</style>
</head>
<body>

<section class="sheet sheet--front">
  <div class="art">
    <svg class="shapes" viewBox="0 0 479 672" width="479" height="672">
      <defs>
        <linearGradient id="site" x1="0" y1="0" x2="0" y2="1">
          <stop offset="0" stop-color="#6b7686"/>
          <stop offset=".55" stop-color="#8a5a5c"/>
          <stop offset="1" stop-color="#b72a30"/>
        </linearGradient>
      </defs>
      <polygon points="0,0 430,0 122,536 0,252" fill="url(#site)" role="img" aria-label="Photo of construction workers on a building site with cranes"/>
      <polyline points="0,262 124,552 446,0" fill="none" stroke="#fff" stroke-width="11"/>
      <polygon points="479,70 372,248 392,248 479,100" fill="var(--slate)"/>
      <polygon points="388,272 479,272 479,120" fill="#fff"/>
      <polygon points="354,672 442,548 479,610 479,672" fill="var(--slate)"/>
      <polygon points="338,672 425,562 432,572 350,672" fill="#fff"/>
    </svg>
    <div class="brand" style="left:46px;top:66px;font-size:22px"><i class="brand__mark"></i>NORVEL HIRE</div>
    <h1 class="front-title">Let Our Team Become Yours.</h1>
    <p class="front-sub">Customized solutions to drive your innovation.</p>
    <div class="front-copy front-copy--pitch">
      <span class="front-copy__line" style="width:198px">Norvel Hire combines the</span>
      <span class="front-copy__line" style="width:210px">best tools in human resource and</span>
      <span class="front-copy__line" style="width:218px">risk management with industry-</span>
      <span class="front-copy__line" style="width:228px">leading knowledge to create a unique</span>
      <span class="front-copy__line front-copy__line--end" style="width:237px">operational platform.</span>
    </div>
    <div class="front-copy front-copy--quote">
      <span class="front-copy__line" style="width:258px">“Our expertise in human resource</span>
      <span class="front-copy__line" style="width:268px">management, risk mitigation and safety,</span>
      <span class="front-copy__line" style="width:280px">payroll administration, workers’ compensation</span>
      <span class="front-copy__line" style="width:287px">coverage and employee benefits allow our</span>
      <span class="front-copy__line front-copy__line--end" style="width:297px">clients to focus on their core business”</span>
    </div>
    <div class="front-url">www.norvelhire.example</div>
  </div>
</section>

<section class="sheet sheet--back">
  <div class="art">
    <svg class="shapes" viewBox="0 0 479 672" width="479" height="672">
      <polygon points="0,0 479,0 479,60 0,72" fill="#e4e4e6"/>
      <polygon points="90,0 479,0 479,70 200,80" fill="var(--slate-dark)" role="img" aria-label="Photo of an office building facade"/>
      <polygon points="0,72 479,60 479,0 479,60 0,100" fill="var(--red)"/>
      <polygon points="0,626 479,562 479,672 0,672" fill="#fff"/>
      <polygon points="0,626 479,562 479,570 0,634" fill="var(--slate)"/>
      <g fill="none" stroke-width="15">
        <path d="M73,132 A56,56 0 0 1 185,132" stroke="var(--slate)"/>
        <path d="M73,132 A56,56 0 0 0 185,132" stroke="#fff"/>
        <path d="M186,132 A56,56 0 0 1 298,132" stroke="#fff"/>
        <path d="M186,132 A56,56 0 0 0 298,132" stroke="var(--slate)"/>
        <path d="M298,132 A56,56 0 0 1 410,132" stroke="var(--slate)"/>
        <path d="M298,132 A56,56 0 0 0 410,132" stroke="#fff"/>
      </g>
      <g fill="#f3b7b0">
        <polygon points="174,128 182,132 174,136"/>
        <polygon points="288,128 296,132 288,136"/>
      </g>
    </svg>
    <div class="stage-ring" style="left:74px;top:124px">Tactical<br>Alignment</div>
    <div class="stage-ring" style="left:187px;top:124px">Supervisor<br>Development</div>
    <div class="stage-ring" style="left:299px;top:124px">Business-level<br>guidance</div>

    <div class="expect-band"></div>
    <h2 class="expect-title">What you can expect from Norvel</h2>
    <p class="intro">Business owners working with Norvel typically move through three stages.</p>

    <div class="stage" style="top:272px">
      <div class="stage__head"><i class="stage__icon"></i><span>Tactical Alignment</span></div>
      <p class="stage__text">The first stage addresses the administrative and tactical components of managing your employees.</p>
      <ul class="stage__list">
        <li>Analysis of safety programs and HR practices</li>
        <li>Establish payroll submission and administration protocol</li>
        <li>Hiring, selection and new hire onboarding best practices</li>
        <li>Injury reporting protocol</li>
        <li>Establishing goals and creation of action plan</li>
        <li>Identification of metrics to track effectiveness</li>
      </ul>
    </div>

    <div class="stage" style="top:378px">
      <div class="stage__head"><i class="stage__icon"></i><span>Supervisor Development</span></div>
      <p class="stage__text">The second stage of the relationship focuses on continuing process improvement, further development of HR, risk and payroll best practices, as well as supervisor development. Examples include:</p>
      <ul class="stage__list">
        <li>Ongoing development and refinement of action plans</li>
        <li>Supervisory skill development and training (workplace safety, effective human capital management, and overall risk mitigation)</li>
        <li>Platform of performance management and performance improvement</li>
        <li>Evaluation of employee benefits options</li>
      </ul>
    </div>

    <div class="stage" style="top:488px">
      <div class="stage__head"><i class="stage__icon"></i><span>Business-level guidance</span></div>
      <p class="stage__text">Activities involved in the third stage of the relationship are more strategic and forward looking with a goal of cultivating an environment in your organization in which employees and supervisors drive the success of the organization instead of you, the business owner. Areas of focus may include:</p>
      <ul class="stage__list">
        <li>Organizational development and design</li>
        <li>Leadership development and succession planning</li>
        <li>Holistic view of where your business is going</li>
        <li>Proactive mitigation of business risks</li>
        <li>Strategic planning</li>
      </ul>
    </div>

    <div class="contact"><b>Contact Info:</b> ☎ 555-014-2290
      <div class="contact__mail">✉ info@norvelhire.example</div>
    </div>
    <div class="socials"><i></i><i></i><i></i></div>
    <div class="back-brand"><i></i>NORVEL HIRE</div>
    <div class="back-url">www.norvelhire.example</div>
  </div>
</section>

</body>
</html>
```